Briefpapier im Word-Format für Sachverständigenbüro
Zielgruppe
Sachverständigenbüro für Sach- und Haftpflichtversicherungsschäden
Aufgabenstellung
Beibehaltung aktueller Logos, Erstellung einer Word-Datei zum selbst ausdrucken und kompatibel für Ausdruck über Word ohne Abschnitt der Seitenränder

```html
<!DOCTYPE html>
<html lang="de">
<head>
<meta charset="utf-8">
<title>Briefpapier Prüfdienst Auental</title>
<link href="https://fonts.googleapis.com/css2?family=Open+Sans:wght@400;600;700&display=swap" rel="stylesheet">
<style>
  :root {
    --backdrop: #d2d2d2;
    --paper: #ffffff;
    --ink: #3a3a3a;
    --ink-soft: #6b6b6b;
    --brand-red: #c8252a;
    --pill: #3b3b3b;
    --watermark: #e3e3e3;
  }
  * { margin: 0; padding: 0; box-sizing: border-box; }
  html, body { width: 1200px; height: 958px; overflow: hidden; }
  body {
    background: var(--backdrop);
    font-family: "Open Sans", Arial, sans-serif;
    color: var(--ink);
    position: relative;
  }
  .sheet {
    position: absolute;
    top: 79px;
    width: 566px;
    height: 800px;
    background: var(--paper);
    box-shadow: 0 6px 18px rgba(0,0,0,0.12);
  }
  .sheet--first { left: 23px; }
  .sheet--follow { left: 611px; }

  .brand { position: absolute; right: 52px; top: 82px; text-align: right; }
  .brand__mark {
    display: block; width: 22px; height: 22px; margin: 0 0 8px auto;
    background: var(--brand-red);
  }
  .brand__name {
    font-size: 11px; font-weight: 700; letter-spacing: 1.6px;
    text-transform: uppercase; color: var(--ink); white-space: nowrap;
  }
  .sheet--first .brand { top: 42px; }

  .sender-line {
    position: absolute; left: 54px; top: 134px;
    font-size: 5px; text-decoration: underline; color: var(--ink);
  }
  .recipient {
    position: absolute; left: 54px; top: 147px;
    font-size: 7.5px; line-height: 11px; color: var(--ink-soft);
    font-style: normal;
  }

  .contact {
    position: absolute; left: 395px; top: 116px;
    border-left: 1.4px solid var(--brand-red);
    padding-left: 7px;
    font-size: 6.8px; line-height: 11.2px; color: var(--ink);
    white-space: nowrap;
  }
  .contact__name { color: var(--brand-red); }
  .contact__row { display: flex; align-items: center; gap: 4px; }
  .contact__row svg { width: 7px; height: 7px; fill: var(--brand-red); }
  .contact__gap { height: 4px; }
  .contact__label { display: inline-block; width: 22px; }

  .fold-mark {
    position: absolute; left: 12px; width: 8px; height: 1px; background: var(--ink);
  }
  .fold-mark--upper { top: 267px; }
  .fold-mark--lower { top: 534px; }

  .letter-body {
    position: absolute; left: 54px; top: 288px; width: 446px;
    font-size: 7.2px; line-height: 11.2px; color: var(--ink-soft);
  }
  .letter-body p { margin-bottom: 8px; }

  .watermark {
    position: absolute; left: 56px; top: 600px;
    font-size: 44px; font-weight: 700; line-height: 50px;
    text-transform: uppercase; letter-spacing: 2px; color: var(--watermark);
  }

  .footer-band {
    position: absolute; left: 13px; right: 14px; top: 776px; height: 12px;
    display: flex; align-items: center;
  }
  .footer-band__line { height: 4px; background: var(--brand-red); }
  .footer-band__line--lead { width: 364px; }
  .footer-band__line--tail { flex: 1; margin-left: 6px; }
  .footer-band__web {
    background: var(--pill); color: #fff; font-size: 6.5px;
    padding: 2px 7px; border-radius: 0 0 4px 4px; white-space: nowrap;
    height: 13px; line-height: 9px; margin-left: 3px;
  }
</style>
</head>
<body>

<section class="sheet sheet--first" aria-label="Briefbogen erste Seite">
  <div class="brand">
    <span class="brand__mark"></span>
    <div class="brand__name">Prüfdienst Auental</div>
  </div>

  <div class="sender-line">Prüfdienst Auental | Lindenweg 7 | 84512 Berghofen</div>
  <address class="recipient">
    Mustermann GmbH<br>Herr Max mustermann<br>Musterstraße 4711<br>08159 Musterstadt
  </address>

  <div class="contact">
    <div class="contact__name">Prüfdienst Auental</div>
    <div>Lindenweg 7</div>
    <div>84512 Berghofen</div>
    <div class="contact__gap"></div>
    <div class="contact__row"><svg viewBox="0 0 10 10"><path d="M2 0.5l2 2-1 1.3c.6 1.3 1.6 2.3 2.9 2.9l1.3-1 2 2-1.4 1.8C4.7 9.2.8 5.3.3 2z"/></svg>08431 / 552190</div>
    <div class="contact__row"><svg viewBox="0 0 10 10"><rect x="2.5" y="0.5" width="5" height="3"/><rect x="0.5" y="3.5" width="9" height="4"/><rect x="2.5" y="7" width="5" height="2.5"/></svg>08431 / 552191</div>
    <div class="contact__row"><svg viewBox="0 0 10 10"><path d="M0.5 2h9v6h-9z M0.5 2l4.5 3.5 4.5-3.5" /></svg>info@pruefdienst-auental.de</div>
    <div class="contact__gap"></div>
    <div>Inhaber: Jonas Weidelbach</div>
    <div>USt ID DE318204657</div>
    <div><span class="contact__label">IBAN:</span>DE12 3456 7800 0011 2233 44</div>
    <div><span class="contact__label">BIC:</span>BERGDEF1XXX</div>
  </div>

  <span class="fold-mark fold-mark--upper"></span>
  <span class="fold-mark fold-mark--lower"></span>

  <div class="letter-body">
    <p>Lorem ipsum dolor sit amet, consetetur sadipscing elitr, sed diam nonumy eirmod tempor invidunt ut labore et dolore magna aliquyam erat, sed diam voluptua. At vero eos et accusam et justo duo dolores et ea rebum. Stet clita kasd gubergren, no sea takimata sanctus est Lorem psum dolor sit amet.</p>
    <p>Lorem ipsum dolor sit amet, consetetur sadipscing elitr, sed diam nonumy eirmod tempor invidunt ut labore et dolore magna aliquyam erat, sed diam voluptua. At vero eos et accusam et justo duo dolores et ea rebum. Stet clita kasd gubergren, no sea takimata s anctus est Lorem ipsum dolor sit amet. Lorem ipsum dolor sit amet, consetetur sadipscing elitr, sed diam nonumy eirmod tempor.</p>
    <p>invidunt ut labore et dolore magna aliquyam erat, sed diam voluptua. At vero eos et accusam et justo duo dolores et ea rebum. Stet clita kasd gubergren, no sea takimata sanctus est Lorem psum dolor sit amet. Lorem ipsum dolor sit amet, consetetur sadipscing elitr, sed diam nonumy eirmod tempor invidunt ut labore et dolore magna aliquyam erat, sed diam voluptua.</p>
    <p>At vero eos et accusam et justo duo dolores et ea rebum. Stet clita kasd gubergren, no sea takimata s anctus est Lorem ipsum dolor sit amet.</p>
  </div>

  <div class="watermark" aria-hidden="true">Prüfdienst<br>Auental</div>

  <div class="footer-band">
    <span class="footer-band__line footer-band__line--lead"></span>
    <span class="footer-band__web">www.pruefdienst-auental.de</span>
    <span class="footer-band__line footer-band__line--tail"></span>
  </div>
</section>

<section class="sheet sheet--follow" aria-label="Briefbogen Folgeseite">
  <div class="brand">
    <span class="brand__mark"></span>
    <div class="brand__name">Prüfdienst Auental</div>
  </div>

  <div class="watermark" aria-hidden="true">Prüfdienst<br>Auental</div>

  <div class="footer-band">
    <span class="footer-band__line footer-band__line--lead"></span>
    <span class="footer-band__web">www.pruefdienst-auental.de</span>
    <span class="footer-band__line footer-band__line--tail"></span>
  </div>
</section>

</body>
</html>
```